Velmint website

A clean uncluttered design that shows at glance that we are in the Media and design and publishing business.

We would like to see designs that use colours that show warmth and quality.

The website should show:
- products
- projects

These should be displaxed in spaces that we can add or interchanges with new products or projects.
Updates

Target Market(s)

Business and project managers and buyers and authors.

Industry/Entity Type

Business

Requirements
Must have
• Good colours. Not too strong, not weak, but reflecting quality.

```html
<!DOCTYPE html>
<html lang="en">
<head>
<meta charset="utf-8">
<title>Velmint — Publishing</title>
<link href="https://fonts.googleapis.com/css2?family=Open+Sans:ital,wght@0,400;0,600;0,700;0,800;1,700;1,800&display=swap" rel="stylesheet">
<style>
:root{
  --green:#5aa82a;
  --green-dark:#3f7d1c;
  --green-light:#8cc63f;
  --nav:#2f5f16;
  --ink:#333;
  --muted:#777;
  --panel:#f4f4f2;
  --line:#d9d9d6;
  --wood:#d9a862;
  --wood-dark:#b9803c;
  --bg:#ececea;
  --white:#fff;
}
*{box-sizing:border-box;margin:0;padding:0}
html,body{width:726px;height:1200px;overflow:hidden}
body{font-family:"Open Sans",Arial,sans-serif;color:var(--ink);background:radial-gradient(ellipse at 50% 40%,#fafaf8 0%,var(--bg) 75%);position:relative;font-size:8px}
.abs{position:absolute}

/* header */
.brand{left:80px;top:8px;display:flex;align-items:center;gap:6px}
.brand-mark{width:20px;height:20px;background:var(--green);border-radius:3px}
.brand-name{font-weight:800;font-size:22px;color:var(--green-dark);letter-spacing:.5px}
.phone{right:78px;top:10px;font-weight:700;font-size:13px;color:var(--green);font-style:italic}
.search-bar{right:120px;top:30px;width:150px;height:15px;border:1px solid var(--line);background:var(--white);border-radius:8px;font-size:6px;color:#aaa;padding:3px 8px}
.search-bar::after{content:"";position:absolute;right:-1px;top:-1px;width:22px;height:15px;background:var(--green);border-radius:0 8px 8px 0}
.cart{right:80px;top:31px;font-size:7px;font-weight:700;display:flex;align-items:center;gap:3px}

.nav{left:78px;top:56px;width:570px;height:20px;background:var(--nav);display:flex;align-items:center;padding-left:0;border-radius:2px}
.nav a{color:#e9f3df;text-decoration:none;font-size:6.3px;padding:0 7px;height:20px;line-height:20px;border-right:1px solid rgba(255,255,255,.12)}
.nav a.active{background:var(--green);color:var(--white);font-weight:700}

/* hero */
.hero{left:78px;top:84px;width:570px;height:232px;background:linear-gradient(100deg,var(--green-light) 0%,var(--green) 45%,var(--green-dark) 100%);border-radius:3px;overflow:hidden}
.hero-copy{left:20px;top:26px;color:var(--white)}
.hero-title{font-style:italic;font-weight:800;font-size:20px;line-height:1.1}
.hero-sub{font-style:italic;font-weight:800;font-size:20px;line-height:1.15;text-transform:uppercase}
.hero-meta{font-size:8px;margin-top:16px;font-weight:600}
.buy{left:20px;top:162px;width:124px;height:30px;background:var(--nav);color:var(--white);font-weight:800;font-style:italic;font-size:13px;display:flex;align-items:center;justify-content:space-between;padding:0 10px;border-radius:3px}
.buy svg{width:14px;height:14px}
.hero-photo{left:250px;top:0;width:320px;height:232px;background:linear-gradient(160deg,#e7efe2 0%,#b8cfa4 55%,#6d8f57 100%)}
.hero-book{left:310px;top:22px;width:80px;height:112px;background:linear-gradient(180deg,#2e6a1a,#143a0c);border:2px solid #fff;box-shadow:2px 3px 6px rgba(0,0,0,.3)}
.hero-dots{left:260px;top:212px;display:flex;gap:4px}
.hero-dots i{width:6px;height:6px;border-radius:50%;background:rgba(255,255,255,.55)}
.hero-dots i:first-child{background:var(--white)}

/* sidebar */
.list-btn{left:80px;top:324px;width:114px;height:17px;background:var(--green);color:var(--white);font-weight:800;font-size:7px;display:flex;align-items:center;padding-left:6px;border-radius:2px}
.box{left:80px;width:114px;background:var(--panel);border:1px solid var(--line);border-radius:3px;overflow:hidden}
.box h3{background:var(--green);color:var(--white);font-size:7px;font-weight:700;padding:4px 6px}
.field{margin:6px 6px 0;height:13px;background:var(--white);border:1px solid var(--line);font-size:5.5px;color:#999;padding:2px 4px}
.small-btn{display:inline-block;background:var(--green);color:var(--white);font-size:6px;font-weight:700;padding:3px 8px;border-radius:2px}
.news{display:flex;gap:4px;margin:6px 6px 0;font-size:5.5px;color:var(--muted);line-height:1.3}
.news b{flex:none;width:14px;height:14px;background:var(--green);color:var(--white);font-size:6px;text-align:center;line-height:14px}

/* main */
.welcome{left:213px;top:326px;width:435px}
.welcome h2{font-size:9px;font-weight:700;color:var(--green-dark);margin-bottom:5px}
.welcome p{font-size:6px;line-height:1.45;margin-bottom:2px}
.welcome .note{color:#999;font-size:5px;margin-top:4px}
.welcome .more{position:absolute;right:0;bottom:-8px;font-size:5px;color:var(--green)}

.shelf{left:213px;width:435px;background:var(--wood);border-radius:4px;border:1px solid var(--wood-dark);overflow:hidden}
.shelf h3{background:linear-gradient(180deg,var(--green-light),var(--green));color:var(--white);font-size:8px;font-weight:700;padding:6px 10px}
.books{display:flex;gap:14px;padding:14px 0 0 52px;height:112px;border-bottom:6px solid var(--wood-dark)}
.book{width:48px;height:88px;box-shadow:2px 2px 4px rgba(0,0,0,.35)}
.more-btn{position:absolute;right:8px;bottom:7px;background:var(--green);color:var(--white);font-size:5.5px;font-weight:700;padding:3px 6px;border-radius:2px}

/* footer */
.foot-nav{left:0;top:1090px;width:726px;display:flex;justify-content:center;gap:8px;font-size:5.5px;color:var(--muted)}
.foot-nav span:first-child{color:var(--green)}
.foot-phone{left:0;top:1110px;width:726px;text-align:center;font-weight:700;font-style:italic;font-size:13px;color:var(--green)}
.foot-brand{left:0;top:1136px;width:726px;display:flex;justify-content:center;align-items:center;gap:5px}
.foot-brand .brand-mark{width:14px;height:14px}
.foot-brand .brand-name{font-size:14px}
.social{left:0;top:1160px;width:726px;display:flex;justify-content:center;gap:5px}
.social i{width:11px;height:11px;border-radius:50%;background:#9a9a98}
.copy{left:0;top:1182px;width:726px;text-align:center;font-size:5px;color:#999}
</style>
</head>
<body>

<header>
  <div class="abs brand"><span class="brand-mark"></span><span class="brand-name">VELMINT</span></div>
  <div class="abs phone">555.014.2290</div>
  <div class="abs search-bar">Search by Book Name</div>
  <div class="abs cart">
    <svg width="12" height="10" viewBox="0 0 12 10"><path d="M0 1h2l1.5 6h6.5l1.5-4.5H3" fill="none" stroke="#333" stroke-width="1.2"/><circle cx="4.5" cy="9" r="1" fill="#333"/><circle cx="9" cy="9" r="1" fill="#333"/></svg>Cart
  </div>
  <nav class="abs nav">
    <a class="active">Home</a><a>About Us</a><a>eBooks</a><a>Free Books</a><a>Printed Books</a><a>New Authors</a><a>Author Registration</a><a>Publisher / Agent</a><a>FAQ</a><a>Contact Us</a>
  </nav>
</header>

<section class="abs hero">
  <div class="abs hero-photo" role="img" aria-label="Photo of the author in cricket whites raising his bat"></div>
  <div class="abs hero-book" role="img" aria-label="Cover of the featured autobiography"></div>
  <div class="abs hero-copy">
    <div class="hero-title">My Autobigtaphy</div>
    <div class="hero-sub">Doyle</div>
    <div class="hero-meta">Author : HARLAN DOYLE, Price: £ 300.00</div>
  </div>
  <div class="abs buy">Buy Now
    <svg viewBox="0 0 14 14"><circle cx="7" cy="7" r="6.5" fill="#fff"/><path d="M5.5 4l3 3-3 3" fill="none" stroke="#2f5f16" stroke-width="1.6"/></svg>
  </div>
  <div class="abs hero-dots"><i></i><i></i><i></i></div>
</section>

<aside>
  <div class="abs list-btn">LIST YOUR BOOK NOW!</div>

  <div class="abs box" style="top:346px;height:140px">
    <h3>Advance Search</h3>
    <div class="field">Search Books</div>
    <div class="field">Search Books</div>
    <div class="field">Search Books</div>
    <div style="margin:8px 6px 0;text-align:right"><span class="small-btn">Search</span></div>
  </div>

  <div class="abs box" style="top:498px;height:136px">
    <h3>Author Login</h3>
    <div class="field">User Name</div>
    <div class="field">Password</div>
    <div style="margin:7px 6px 0;display:flex;gap:5px"><span class="small-btn">Login</span><span class="small-btn">Clear</span></div>
    <div style="margin:6px 6px 0;font-size:5px;color:var(--muted);line-height:1.4">Not registered yet?<br><b style="color:var(--ink)">Register now</b> · Forgot password</div>
  </div>

  <div class="abs box" style="top:652px;height:148px">
    <h3>Latest News</h3>
    <div class="news"><b>12</b><span>Lorem ipsum is simply dummy text of the</span></div>
    <div class="news"><b>14</b><span>Lorem ipsum is simply dummy text of the</span></div>
    <div class="news"><b>18</b><span>Lorem ipsum is simply dummy text of the</span></div>
    <div style="margin:8px 6px 0;text-align:right;font-size:5.5px;color:var(--green)">More</div>
  </div>

  <div class="abs box" style="top:816px;height:100px">
    <h3>Signup to a newsletter</h3>
    <div class="field">Name</div>
    <div class="field">Email</div>
    <div style="margin:8px 6px 0"><span class="small-btn">Subscribe now</span></div>
  </div>
</aside>

<main>
  <section class="abs welcome">
    <h2>Welcome to Velmint Publishes Book</h2>
    <p><b>"The ebook resource for authors, writers and readers."</b></p>
    <p><b>Don't let your creativity go to waste!</b></p>
    <p>Publish your short stories, articles and unpublished books and reach a global audience. If enough of our readers enjoy what you write then we can help you secure that elusive book publishing deal!</p>
    <p class="note">Turning fresh manuscripts into printed and digital books for new authors</p>
    <span class="more">Read more</span>
  </section>

  <section class="abs shelf" style="top:460px;height:180px">
    <h3>Our Products</h3>
    <div class="books">
      <div class="book" role="img" aria-label="Book cover" style="background:linear-gradient(#c9a27a,#6b3f2a)"></div>
      <div class="book" role="img" aria-label="Book cover" style="background:linear-gradient(#e7c9c2,#8a3b4a)"></div>
      <div class="book" role="img" aria-label="Book cover" style="background:linear-gradient(#6b8fb5,#1f3550)"></div>
      <div class="book" role="img" aria-label="Book cover" style="background:linear-gradient(#d5d9c2,#526b3a)"></div>
      <div class="book" role="img" aria-label="Book cover" style="background:linear-gradient(#a9c8df,#2c4e73)"></div>
    </div>
    <span class="more-btn">View More Books</span>
  </section>

  <section class="abs shelf" style="top:658px;height:192px">
    <h3>Latest free books</h3>
    <div class="books">
      <div class="book" role="img" aria-label="Book cover" style="background:linear-gradient(#3a4a6a,#151d2e)"></div>
      <div class="book" role="img" aria-label="Book cover" style="background:linear-gradient(#d43a2f,#8c1c16)"></div>
      <div class="book" role="img" aria-label="Book cover" style="background:linear-gradient(#e8d6b8,#9a6a3a)"></div>
      <div class="book" role="img" aria-label="Book cover" style="background:linear-gradient(#f2efe4,#b5a98a)"></div>
      <div class="book" role="img" aria-label="Book cover" style="background:linear-gradient(#7fa7c9,#3d5f7d)"></div>
    </div>
    <span class="more-btn">View More Books</span>
  </section>

  <section class="abs shelf" style="top:870px;height:195px">
    <h3>Latest Printed Books</h3>
    <div class="books">
      <div class="book" role="img" aria-label="Book cover" style="background:linear-gradient(#f0a63a,#c0641c)"></div>
      <div class="book" role="img" aria-label="Book cover" style="background:linear-gradient(#f1e7d2,#b79b6a)"></div>
      <div class="book" role="img" aria-label="Book cover" style="background:linear-gradient(#5b7a3a,#233a14)"></div>
      <div class="book" role="img" aria-label="Book cover" style="background:linear-gradient(#9b3b3b,#3d1414)"></div>
      <div class="book" role="img" aria-label="Book cover" style="background:linear-gradient(#c7d7e4,#55708a)"></div>
    </div>
    <span class="more-btn">View More Books</span>
  </section>
</main>

<footer>
  <div class="abs foot-nav"><span>Home</span><span>About Us</span><span>eBooks</span><span>Free Books</span><span>Printed Books</span><span>New Authors</span><span>Author Registration</span><span>Publisher / Agent</span><span>FAQ</span><span>Sitemap</span><span>Affiliates</span><span>Contact Us</span></div>
  <div class="abs foot-phone">555.014.2290</div>
  <div class="abs foot-brand"><span class="brand-mark"></span><span class="brand-name">VELMINT</span></div>
  <div class="abs social"><i></i><i></i><i></i><i></i><i></i><i></i></div>
  <div class="abs copy">© 2013 Velmint. All Rights Reserved.</div>
</footer>

</body>
</html>
```